依頼詳細
高級住宅地、オフィス街を対象に配るA4チラシ(片面)になります。高級感溢れるデザインをお願いいたします。
印刷はミドリカゼを使用する予定です。入稿可能なAiファイルでの作成をお願いいたします。
https://midorikaze-example.jp/dataguide/

色選びはカラーパレットをご使用ください。
記載項目
記載内容は添付のワードファイルをご参照ください。
講師プロフィール用の写真は仮の写真です。決定いたしまた方に後ほど実際に使用いただく写真をお渡しいたします。
イメージ画像を1枚添付しておりますが、使用はお任せいたします。
サイズ
A4
ページ数
片面
希望イメージ
シンプル 複雑
単色 カラフル
暗い 明るい
日常 高級
遊び心 厳粛
未来的 伝統的
女性的 男性的
希望する色
黄・オレンジ系、青系、無彩色系
納品ファイル
• イラストレーター形式 (.ai)
補足説明
当初の設定ミスで募集期間5日間としていましたが、3日間に訂正いたします。
期間が短くなりますが、どうぞよろしくお願いいたします。
報酬金額変更いたしました。
どうぞよろしくお願いいたします。
提出ファイル形式についての追記です。
採用に至った場合は、そのまま入稿できるAiファイルと後に文字を編集する予定があるためテキストをアウトライン化する前(テキスト部分が後に編集できるもの)のファイルの2種類の提出をお願いいたします。可能であればWindows Adobe Illustrator CS4対応のファイル形式でお願いします。また、特殊なフォントをご使用の場合は一緒にご提出願います。
お手数おかけいたしますがよろしくお願いいたします。

ターゲットを意識した画像の使用、レイアウト、高級感とすべてよかったです。

この度はコンペにご参加いただきありがとうございました。
予想以上に多くの提案をいただきまして大変感謝いたしております。
多数の素晴らしいご提案から選ぶのに時間がかかりまして、
お待たせいたしましたことをお詫び申し上げます。
また、機会がございましたらどうぞよろしくお願いいたします。

```html
<!DOCTYPE html>
<html lang="ja">
<head>
<meta charset="utf-8">
<title>KAVRA ビジネス英会話 プライベートレッスン</title>
<link href="https://fonts.googleapis.com/css2?family=Noto+Serif+JP:wght@400;600;700&family=Noto+Sans+JP:wght@400;500;700&display=swap" rel="stylesheet">
<style>
  :root{
    --navy-deep:#0a1330;
    --navy:#14224a;
    --navy-mid:#243a6e;
    --blue-soft:#7e9bcb;
    --blue-pale:#b9cbe6;
    --ink:#1d2438;
    --paper:#f3f5f9;
    --white:#ffffff;
    --muted:#c9d3e6;
    --line:#4a6399;
  }
  *{margin:0;padding:0;box-sizing:border-box}
  html,body{width:849px;height:1200px;overflow:hidden;background:var(--paper)}
  body{font-family:"Noto Sans JP",sans-serif;color:var(--ink)}
  .flyer{position:relative;width:849px;height:1200px;overflow:hidden;background:var(--paper)}

  .hero{position:absolute;left:0;top:0;width:849px;height:870px;
    background:linear-gradient(165deg,var(--navy-deep) 0%,var(--navy) 50%,var(--navy-mid) 100%)}
  .hero-photo{position:absolute;right:0;top:0;width:470px;height:480px;
    background:linear-gradient(200deg,#8a8f9c 0%,#4d5568 45%,#1a2548 100%)}
  .hero-photo::after{content:"";position:absolute;inset:0;
    background:linear-gradient(90deg,var(--navy-deep) 0%,rgba(10,19,48,0) 40%)}
  .brand{position:absolute;right:36px;top:20px;font-family:"Noto Serif JP",serif;
    font-weight:600;font-size:15px;letter-spacing:3px;color:var(--white);display:flex;align-items:center;gap:6px}
  .brand-mark{width:8px;height:8px;background:var(--white)}
  .headline{position:absolute;left:40px;top:44px;font-family:"Noto Serif JP",serif;
    font-weight:600;font-size:52px;line-height:1.45;color:var(--white);letter-spacing:3px}
  .lead{position:absolute;left:40px;top:330px;width:320px;font-size:9.5px;line-height:1.8;color:var(--muted)}

  .info{position:absolute;left:0;top:480px;width:849px;height:150px;
    background:rgba(10,19,48,.72);border-top:1px solid var(--line);border-bottom:1px solid var(--line)}
  .info-block{position:absolute;top:16px;font-size:9px;line-height:1.8;color:var(--muted)}
  .info-block h3{font-size:11px;font-weight:700;color:var(--white);margin-bottom:6px;letter-spacing:1px}
  .info-limited{left:40px;width:260px}
  .info-limited h3{display:inline-block;border-bottom:1px solid var(--white)}
  .info-recruit{left:340px;width:230px;border-left:1px solid var(--line);padding-left:16px}
  .info-fee{left:600px;width:220px;border-left:1px solid var(--line);padding-left:16px}

  .why-title{position:absolute;left:0;top:650px;width:849px;text-align:center;
    font-family:"Noto Serif JP",serif;font-size:20px;line-height:1.4;font-weight:600;color:var(--white);letter-spacing:2px}
  .reasons{position:absolute;left:40px;top:700px;width:769px;display:flex;gap:16px}
  .reason{flex:1}
  .reason-head{height:50px;display:flex;align-items:center;justify-content:center;
    background:linear-gradient(180deg,var(--blue-pale),var(--blue-soft));
    border:1px solid var(--white);font-size:11px;line-height:1.5;font-weight:700;color:var(--navy-deep);text-align:center}
  .reason-body{margin-top:10px;font-size:8.5px;line-height:1.75;color:var(--muted)}

  .profile{position:absolute;left:40px;top:888px;width:769px;height:250px;background:var(--white);
    border:1px solid #d4dbe8}
  .quote-band{position:absolute;left:0;top:0;width:100%;height:50px;background:var(--navy);padding:8px 18px}
  .quote-ja{font-family:"Noto Serif JP",serif;font-size:14px;line-height:1.4;color:var(--white);letter-spacing:1px}
  .quote-en{font-size:8.5px;line-height:1.4;color:var(--muted);margin-top:2px;font-style:italic}
  .tutor-photo{position:absolute;left:18px;top:62px;width:92px;height:172px;
    background:linear-gradient(180deg,#c7cdd8 0%,#5c6780 50%,#1d2640 100%)}
  .tutor-intro{position:absolute;left:124px;top:60px;width:270px;font-size:8px;line-height:1.7}
  .tutor-intro h4{font-family:"Noto Serif JP",serif;font-size:11px;color:var(--navy);margin-bottom:3px}
  .career{position:absolute;left:124px;top:158px;width:270px;font-size:8px;line-height:1.65}
  .career h4{font-size:9px;color:var(--navy);margin-bottom:2px;border-bottom:1px solid var(--navy);display:inline-block}
  .faq{position:absolute;left:410px;top:60px;width:342px;height:178px;border:1px solid var(--navy);padding:7px 12px}
  .faq h4{font-size:9.5px;color:var(--navy);margin-bottom:2px}
  .faq dl{font-size:7.5px;line-height:1.5}
  .faq dt{font-weight:700;color:var(--navy);margin-top:3px}
  .faq dt::before{content:"Q. "}
  .faq dd::before{content:"A. ";font-weight:700;color:var(--navy)}

  .footer{position:absolute;left:0;top:1150px;width:849px;height:50px;background:var(--navy-deep);
    display:flex;align-items:center;justify-content:space-between;padding:0 40px;color:var(--white)}
  .footer-lead{font-family:"Noto Serif JP",serif;font-size:13px}
  .footer-contact{font-size:9px;color:var(--muted);display:flex;gap:14px;align-items:center}
  .footer-contact svg{vertical-align:middle;margin-right:3px}
</style>
</head>
<body>
<main class="flyer">
  <section class="hero">
    <div class="hero-photo" role="img" aria-label="新聞を読むスーツ姿のビジネスマンの写真"></div>
    <div class="brand"><span class="brand-mark"></span>KAVRA</div>
    <h1 class="headline">全てにおいて<br>最高品質を<br>求める貴方へ</h1>
    <p class="lead">CEO、経営者、医師、弁護士、大学教授、ジャーナリストなど、多忙なエリートの皆様に向けた完全マンツーマンの英会話レッスン。経験豊富な講師が、貴方のご都合に合わせて最高水準のプライベートレッスンをお届けします。</p>

    <div class="info">
      <div class="info-block info-limited">
        <h3>限定案内</h3>
        <p>ご自宅またはオフィスへ講師が伺うプライベートレッスンです。講師のスケジュールの都合上、受講枠には限りがございます。お早めにお申し込みください。</p>
      </div>
      <div class="info-block info-recruit">
        <h3>【募集中】</h3>
        <p>火曜日 13:00〜20:00<br>木曜日 13:00〜20:00<br>場所：ご自宅・オフィス・指定場所<br>対象：中級〜上級の方</p>
      </div>
      <div class="info-block info-fee">
        <h3>【料金】</h3>
        <p>初回体験レッスン 無料<br>レッスン料 60分 15,000円<br>月4回コース 55,000円（税別）<br>※交通費は別途頂戴いたします</p>
      </div>
    </div>

    <h2 class="why-title">なぜ、レオンのレッスンはそんなに人気なのか？</h2>

    <div class="reasons">
      <div class="reason">
        <div class="reason-head">ビジネスの現場で使える英語</div>
        <p class="reason-body">会議、交渉、プレゼンなど実際の場面を想定し、すぐに役立つ表現を身につけます。</p>
      </div>
      <div class="reason">
        <div class="reason-head">貴方の目的に合わせた<br>完全オーダーメイド</div>
        <p class="reason-body">目標とご要望を丁寧に伺い、一人ひとりに最適な教材とカリキュラムを作成します。</p>
      </div>
      <div class="reason">
        <div class="reason-head">上達への明確な<br>アドバイスを提供</div>
        <p class="reason-body">毎回のレッスンで課題を整理し、確実に成果へつながる学習方法をお伝えします。</p>
      </div>
    </div>
  </section>

  <section class="profile">
    <div class="quote-band">
      <p class="quote-ja">「私のゴールは、一人でも多く日本という国を強くすることです。」</p>
      <p class="quote-en">My goal is to make the country of Japan stronger, one person at a time.</p>
    </div>
    <div class="tutor-photo" role="img" aria-label="スーツ姿の講師のプロフィール写真"></div>
    <div class="tutor-intro">
      <h4>講師 レオン・ハーグレイヴ</h4>
      <p>英国出身。国際企業での勤務経験を活かし、日本で二十年以上にわたりビジネス英語を指導。経営層を中心に多くの受講生から厚い信頼を得ています。丁寧で的確な指導が好評です。</p>
    </div>
    <div class="career">
      <h4>【経歴・実績】</h4>
      <p>・英国の大学にて経営学修士を取得<br>・外資系企業にて海外事業部門を担当<br>・大手企業の役員向け英語研修を多数実施<br>・通訳・翻訳、各種講演の実績多数</p>
    </div>
    <div class="faq">
      <h4>【FAQ】</h4>
      <dl>
        <dt>レッスンは何回から受けられますか？</dt>
        <dd>一回からお申し込みいただけます。まずは無料体験をどうぞ。</dd>
        <dt>英語がほとんど話せなくても大丈夫ですか？</dt>
        <dd>はい。レベルに合わせて内容を調整いたしますのでご安心ください。</dd>
        <dt>日程の変更はできますか？</dt>
        <dd>前日までにご連絡いただければ、振替が可能です。</dd>
        <dt>オンラインでの受講は可能ですか？</dt>
        <dd>ご希望に応じてオンラインでのレッスンも承っております。</dd>
        <dt>支払い方法を教えてください。</dt>
        <dd>銀行振込にてお願いしております。詳細はお問合せください。</dd>
      </dl>
    </div>
  </section>

  <footer class="footer">
    <p class="footer-lead">ご質問等ございましたら、お気軽にお問合せください。</p>
    <div class="footer-contact">
      <span><svg width="10" height="10" viewBox="0 0 10 10"><rect x="0.5" y="1.5" width="9" height="7" fill="none" stroke="#c9d3e6"/><path d="M0.5 1.5 L5 5.5 L9.5 1.5" fill="none" stroke="#c9d3e6"/></svg>info@kavra-english.example</span>
      <span><svg width="10" height="10" viewBox="0 0 10 10"><path d="M2 1 L4 1 L4.6 3 L3.4 4 Q4.5 6 6 6.6 L7 5.4 L9 6 L9 8 Q5 9.5 1 3 Z" fill="#c9d3e6"/></svg>03-0000-1234</span>
      <span>携帯 090-0000-5678</span>
    </div>
  </footer>
</main>
</body>
</html>
```